Bright Summit Consulting Website Design

I already have a live website. Just want some help with design, finishing up the project. I also have another site with wix that I am ready to have designed. I am not completely sure on the pages but will for sure need "coaching", "training", "resources". Most of the people I currently work with are real estate brokers and mortgage brokers but I want to be able to appeal to all industries.
Number of Pages Required
4 page
Font styles to use
Sans Serif
Colors
Designer to choose colors to be used in the design.
Requirements
Must have
- place holders for video
Nice to have
- a way for people to purchase digital downloads

```html
<!DOCTYPE html>
<html lang="en">
<head>
<meta charset="utf-8">
<title>Bright Summit Consulting</title>
<link href="https://fonts.googleapis.com/css2?family=Lato:wght@400;700;900&display=swap" rel="stylesheet">
<style>
:root{
  --red:#e31b23;
  --slate:#3d454d;
  --slate-dark:#2b3137;
  --ink:#333;
  --muted:#555;
  --light:#f2f2f2;
  --white:#fff;
}
*{margin:0;padding:0;box-sizing:border-box}
html,body{width:1200px;height:2432px;overflow:hidden}
body{font-family:"Lato",Arial,sans-serif;color:var(--ink);background:var(--white);position:relative}
.abs{position:absolute}

.site-header{position:absolute;left:0;top:0;width:1200px;height:94px;background:var(--white)}
.brand{position:absolute;left:75px;top:22px;display:flex;align-items:center;gap:10px}
.brand-mark{width:48px;height:48px;background:var(--red)}
.brand-name{font-weight:900;font-size:22px;line-height:24px;color:var(--slate);letter-spacing:.5px;width:230px}
.main-nav a{position:absolute;top:40px;font-size:13px;font-weight:700;color:var(--ink);text-decoration:none;letter-spacing:.3px}
.main-nav a.active{color:var(--red)}
.nav-underline{position:absolute;left:616px;top:62px;width:81px;height:3px;background:var(--red)}

.hero{position:absolute;left:0;top:94px;width:1200px;height:568px;background:linear-gradient(180deg,#b9c4cd 0%,#8d98a2 45%,#3a3f45 100%)}
.hero-band{position:absolute;left:0;top:375px;width:1200px;height:193px;background:rgba(20,22,25,.82);text-align:center;color:var(--white)}
.hero-title{font-size:42px;font-weight:700;margin-top:20px;letter-spacing:.5px}
.hero-text{font-size:19.5px;font-weight:700;line-height:29px;margin-top:8px}

.service-card{position:absolute;top:720px;width:330px;height:462px;background:var(--slate);color:var(--white);text-align:center}
.service-photo{position:absolute;left:16px;top:16px;width:298px;height:196px;background:linear-gradient(160deg,#c9cfd4,#7f8891)}
.service-title{position:absolute;left:0;top:231px;width:100%;font-size:19px;font-weight:700;line-height:24px;letter-spacing:.3px}
.service-text{position:absolute;left:20px;top:292px;width:290px;font-size:13.5px;line-height:24px}

.about{position:absolute;left:0;top:1240px;width:1200px;height:370px}
.about-copy{position:absolute;left:0;top:0;width:613px;height:370px;background:var(--light)}
.about-title{position:absolute;left:75px;top:45px;font-size:34px;font-weight:400;color:var(--red)}
.about-text{position:absolute;left:75px;top:104px;width:520px;font-size:15px;line-height:27.5px;color:var(--muted)}
.btn{display:flex;align-items:center;justify-content:center;background:var(--red);color:var(--white);font-size:12px;font-weight:700;letter-spacing:.3px}
.about-btn{position:absolute;left:75px;top:271px;width:118px;height:34px}
.video{position:absolute;left:613px;top:0;width:587px;height:370px;background:linear-gradient(135deg,#cfc6b8,#8a7f72 55%,#3c3631)}
.video-play{position:absolute;left:270px;top:161px}
.video-caption{position:absolute;right:45px;bottom:8px;text-align:right;color:#e8e8e8;font-weight:700;line-height:28px}
.video-caption .name{font-size:29px}
.video-caption .role{font-size:23px}

.testimonial{position:absolute;left:0;top:1610px;width:1200px;height:151px;text-align:center}
.testimonial q{position:absolute;left:0;top:57px;width:100%;font-size:21px;color:var(--red);quotes:"\201C\00A0" "\201D"}
.testimonial cite{position:absolute;left:0;top:95px;width:100%;font-style:normal;font-size:14.5px;font-weight:700;color:var(--muted)}

.contact{position:absolute;left:0;top:1761px;width:1200px;height:600px;background:var(--slate);color:var(--white)}
.contact-title{position:absolute;left:0;top:50px;width:100%;text-align:center;font-size:34px;font-weight:400}
.map{position:absolute;left:75px;top:131px;width:512px;height:406px;background:linear-gradient(150deg,#e6e6e4,#d3d4d1)}
.office{position:absolute;left:665px;top:125px;width:460px;text-align:center;font-size:15px;line-height:24px}
.office h3{font-size:26px;font-weight:400;line-height:32px;margin-bottom:4px}
.field{position:absolute;left:666px;width:459px;height:34px;background:var(--white);color:var(--ink);font-size:12px;padding:9px 12px}
.field.message{height:83px}
.send-btn{position:absolute;left:945px;top:501px;width:180px;height:36px}

.site-footer{position:absolute;left:0;top:2361px;width:1200px;height:71px;background:var(--slate-dark);color:var(--white)}
.copyright{position:absolute;left:75px;top:26px;font-size:13px}
.social{position:absolute;right:75px;top:27px;display:flex;gap:18px}
.social span{width:16px;height:16px;border-radius:50%;background:var(--white)}
</style>
</head>
<body>

<header class="site-header">
  <div class="brand">
    <div class="brand-mark"></div>
    <div class="brand-name">BRIGHT SUMMIT CONSULTING</div>
  </div>
  <nav class="main-nav">
    <a class="active" style="left:640px">HOME</a>
    <a style="left:717px">ABOUT US</a>
    <a style="left:817px">BOOK ONLINE</a>
    <a style="left:942px">CONTACT</a>
    <a style="left:1040px">CLIENT LOG IN</a>
  </nav>
  <div class="nav-underline"></div>
</header>

<section class="hero" role="img" aria-label="Photo of a business coach presenting to a team around a meeting table">
  <div class="hero-band">
    <h1 class="hero-title">IT'S GROW TIME</h1>
    <p class="hero-text">From making strategic decisions to developing your capabilities, I’m here to help.<br>Using my expertise and deep understanding of the industry, you’ll receive real solutions and<br>experience true results. Get in touch to book a meeting.</p>
  </div>
</section>

<article class="service-card" style="left:75px">
  <div class="service-photo" role="img" aria-label="Photo of a team collaborating at a table"></div>
  <h2 class="service-title">BUSINESS PERFORMANCE<br>CONSULTING</h2>
  <p class="service-text">By analyzing your systems, tools and people,<br>I will identify strategies to get your business<br>running at optimal efficiency.<br>Book an introductory meeting today to learn<br>more about how I can make your<br>business thrive.</p>
</article>
<article class="service-card" style="left:435px">
  <div class="service-photo" role="img" aria-label="Photo of a coach leading a meeting in a glass office"></div>
  <h2 class="service-title">LEADERSHIP BUSINESS<br>COACHING</h2>
  <p class="service-text">Whether just starting out or looking to break<br>through the invisible ceiling, we will work<br>together on keeping you focused on the lead<br>measures that will generate measurable<br>results. Contact me to find out how<br>I can help today.</p>
</article>
<article class="service-card" style="left:795px">
  <div class="service-photo" role="img" aria-label="Photo of a speaker at a podium addressing an audience"></div>
  <h2 class="service-title">SPEAKING AND<br>TRAINING</h2>
  <p class="service-text">Whether you need a single keynote or a<br>training package for your organization, we will<br>collaborate with you as a partner to design a<br>package to take your team to the next level.<br>To find out more, get in touch.</p>
</article>

<section class="about">
  <div class="about-copy">
    <h2 class="about-title">About Our Company</h2>
    <p class="about-text">I’ve been a professional Business Coach since 2010. I believe in maintaining<br>a positive mindset, creating partnerships with a purpose, and always<br>striving for significant outcomes. When you work with me, you should<br>expect a collaboration with transparency and consistency.<br>Want to learn more? Contact me today for an initial consultation.</p>
    <a class="btn about-btn">READ MORE</a>
  </div>
  <div class="video" role="img" aria-label="Video placeholder: introduction from the team leader seated in an office">
    <svg class="video-play" width="46" height="46" viewBox="0 0 46 46" aria-hidden="true">
      <circle cx="23" cy="23" r="22" fill="#fff"/>
      <path d="M18 13 L33 23 L18 33 Z" fill="#222"/>
    </svg>
    <div class="video-caption"><div class="name">Marco Velden</div><div class="role">Team Leader/CEO</div></div>
  </div>
</section>

<section class="testimonial">
  <q>Amazing speaker and motivator. He will light a fire under your a*s!</q>
  <cite>Daniel Moreau</cite>
</section>

<section class="contact">
  <h2 class="contact-title">Contact Us</h2>
  <div class="map" role="img" aria-label="Street map showing the office location">
    <svg class="abs" style="left:145px;top:160px" width="30" height="40" viewBox="0 0 30 40" aria-hidden="true">
      <path d="M15 39 C15 39 2 22 2 14 A13 13 0 0 1 28 14 C28 22 15 39 15 39 Z" fill="#d9262c"/>
      <circle cx="15" cy="14" r="5" fill="#8e1418"/>
    </svg>
  </div>
  <div class="office">
    <h3>Norvane AG</h3>
    <p>214 Harbor Lane Street,<br>Bayview, CA 94000</p>
    <p style="margin-top:5px">Telephone 555.014.2290<br>E-Mail hello@brightsummit.example</p>
  </div>
  <div class="field" style="top:285px">Name</div>
  <div class="field" style="top:326px">Email Address</div>
  <div class="field" style="top:365px">Subject</div>
  <div class="field message" style="top:407px">Message</div>
  <a class="btn send-btn">SEND</a>
</section>

<footer class="site-footer">
  <p class="copyright">Copyright © 2019. Company Name. All Right Reserved</p>
  <div class="social" aria-label="Social links"><span></span><span></span><span></span><span></span><span></span><span></span></div>
</footer>

</body>
</html>
```